High-end Packaging Design For Permanent Holiday Lights

We need a design for our product box for our company HaloSpan which sells permanent Christmas lights.
Box dimensions: 12.69 X 12.69 X 2.06
The box contains a starter kit and lights for customers who want to install their own permanent holiday lights. We want to see classy minimalistic designs the incorporate our logo and brand guidelines.

More white space and use of our logo.

Do not use random imagines of Christmas lights or weird shapes for the design.

This should mimic the style of an orvane zumrik packaging or high end laptop etc.

Target Market(s)

35+ men and women who love the holidays

Industry/Entity Type

Holiday lights

Font styles to use
Other font styles liked:
• Gotham

Requirements
Must have
• Must have our logo, must be classy/high end, must give multiple color options.
Nice to have
• Possible raised foil logo, or different ideas for our logo elements, play around with layouts for the box dimensions.
Should not have
• shouldn't contain any Christmas design elements as our product is used year round,

```html
<!DOCTYPE html>
<html lang="en">
<head>
<meta charset="utf-8">
<title>HaloSpan – Permanent Holiday Lights Box</title>
<link rel="stylesheet" href="https://fonts.googleapis.com/css2?family=Montserrat:ital,wght@0,400;0,600;0,700;0,800;1,700&display=swap">
<style>
  :root {
    --backdrop: #ececec;
    --panel: #fafafa;
    --ink: #3d3d3d;
    --red: #e0262c;
    --orange: #ef8a1f;
    --yellow: #e9bf1a;
    --green: #4fae45;
    --teal: #2aa6a0;
    --blue: #3b5fb0;
    --purple: #8a47a8;
    --pink: #e8438f;
  }
  * { margin: 0; padding: 0; box-sizing: border-box; }
  html, body { width: 1200px; height: 1200px; overflow: hidden; }
  body {
    background: linear-gradient(180deg, #f1f1f1 0%, var(--backdrop) 100%);
    font-family: "Montserrat", Arial, sans-serif;
    position: relative;
  }
  .brand-lockup {
    position: absolute;
    left: 90px;
    top: 240px;
    display: flex;
    align-items: center;
    gap: 18px;
  }
  .brand-dot {
    width: 34px; height: 34px; border-radius: 50%;
    background: var(--ink);
  }
  .brand-name {
    font-size: 46px;
    font-weight: 600;
    letter-spacing: 0.22em;
    color: var(--ink);
    text-transform: uppercase;
  }
  .box-front {
    position: absolute;
    left: 330px;
    top: 360px;
    width: 560px;
    height: 560px;
    background: var(--panel);
    box-shadow: 0 30px 60px rgba(0,0,0,0.12), 0 4px 10px rgba(0,0,0,0.06);
  }
  .box-artwork {
    position: absolute;
    left: 30px;
    top: 40px;
    width: 250px;
    height: 400px;
    border-radius: 8px;
    background: linear-gradient(160deg, rgba(224,38,44,0.14), rgba(233,191,26,0.14) 40%, rgba(79,174,69,0.14) 70%, rgba(59,95,176,0.14));
  }
  .box-brand {
    position: absolute;
    left: 310px;
    top: 120px;
    font-size: 22px;
    font-weight: 600;
    letter-spacing: 0.2em;
    color: var(--ink);
    text-transform: uppercase;
  }
  .box-headline {
    position: absolute;
    left: 310px;
    top: 190px;
    font-size: 36px;
    font-weight: 800;
    line-height: 1.12;
    text-transform: uppercase;
  }
  .box-headline span {
    display: block;
    background: linear-gradient(90deg, var(--red), var(--orange) 45%, var(--yellow) 70%, var(--green));
    -webkit-background-clip: text;
    background-clip: text;
    color: transparent;
  }
  .box-tagline {
    position: absolute;
    left: 60px;
    right: 40px;
    bottom: 50px;
    font-size: 15px;
    font-weight: 700;
    font-style: italic;
    line-height: 1.35;
    text-align: center;
    background: linear-gradient(90deg, var(--pink), var(--red) 25%, var(--orange) 50%, var(--yellow) 70%, var(--green) 85%, var(--teal));
    -webkit-background-clip: text;
    background-clip: text;
    color: transparent;
  }
  .caption {
    position: absolute;
    right: 138px;
    top: 990px;
    font-size: 21px;
    font-weight: 700;
    line-height: 1.3;
    color: var(--ink);
    text-align: right;
  }
</style>
</head>
<body>
  <div class="brand-lockup">
    <div class="brand-dot"></div>
    <div class="brand-name">HaloSpan</div>
  </div>

  <section class="box-front">
    <div class="box-artwork" role="img" aria-label="Rainbow line illustration of hanging ornaments, snowflakes and scattered coloured dots"></div>
    <div class="box-brand">HaloSpan</div>
    <h1 class="box-headline">
      <span>Permanen</span>
      <span>Holiday</span>
      <span>Lights</span>
    </h1>
    <p class="box-tagline">Lorem Ipsum is simply dummy text of the<br>printing and typesetting industry.</p>
  </section>

  <p class="caption">Lorem Ipsum is simply dummy text of the<br>printing and typesetting industry.</p>
</body>
</html>
```